Ostrel Appraisals BV business cards (a financial services company)

I am looking for a business card design that stands out in the financial advisory field of business & intellectual property valuation. The business card design should be conservative, yet different. Address details have changed since the attached business card. New address is:

Molenvlietkade 27
4817 KT Leiden
The Netherlands

Telephone number remains the same.

```html
<!DOCTYPE html>
<html lang="en">
<head>
<meta charset="utf-8">
<title>Ostrel Appraisals BV – Business Cards</title>
<link href="https://fonts.googleapis.com/css2?family=Cinzel:wght@400;600&display=swap" rel="stylesheet">
<style>
  :root {
    --page-bg: #e9e9ea;
    --card-dark: #231f20;
    --stripe-dark: #808080;
    --text-on-dark: #d6d6d6;
    --card-light: #c8c9cb;
    --stripe-light: #ffffff;
    --text-on-light: #6d6e71;
  }
  * { margin: 0; padding: 0; box-sizing: border-box; }
  html, body { width: 1200px; height: 1200px; overflow: hidden; }
  body {
    background: var(--page-bg);
    font-family: "Cinzel", serif;
    position: relative;
  }
  .card {
    position: absolute;
    left: 363px;
    width: 474px;
    height: 268px;
    overflow: hidden;
  }
  .card--front { top: 250px; background: var(--card-dark); color: var(--text-on-dark); }
  .card--back { top: 682px; background: var(--card-light); color: var(--text-on-light); }
  .card__stripes { position: absolute; inset: 0; width: 100%; height: 100%; }
  .card--front .stripe { fill: var(--stripe-dark); }
  .card--back .stripe { fill: var(--stripe-light); }
  .card__content {
    position: absolute; inset: 0;
    text-align: center;
  }
  .wordmark {
    position: absolute; left: 0; right: 0;
    font-weight: 400;
    font-size: 27px;
    letter-spacing: 1px;
    text-transform: uppercase;
  }
  .card--front .wordmark { top: 150px; }
  .card--back .wordmark { top: 108px; }
  .holder {
    position: absolute; left: 0; right: 0; top: 228px;
    line-height: 1.15;
  }
  .holder__name { font-size: 12px; letter-spacing: 0.6px; }
  .holder__role { font-size: 9px; letter-spacing: 0.4px; }
  .tagline {
    position: absolute; left: 0; right: 0; top: 155px;
    font-size: 10px; line-height: 1.25; letter-spacing: 0.5px;
    text-transform: uppercase;
  }
  .contacts {
    position: absolute; left: 0; right: 0; top: 231px;
    font-size: 8.5px; letter-spacing: 0.2px;
    line-height: 1.9;
  }
  .contacts__row { display: flex; justify-content: center; align-items: center; gap: 8px; }
  .contact { display: inline-flex; align-items: center; gap: 3px; }
  .contact svg { width: 11px; height: 11px; fill: var(--text-on-light); }
</style>
</head>
<body>

<section class="card card--front" aria-label="Business card front">
  <svg class="card__stripes" viewBox="0 0 379 214" preserveAspectRatio="none" aria-hidden="true">
    <polygon class="stripe" points="55,0 83,0 0,127 0,84"/>
    <polygon class="stripe" points="90,0 117,0 0,179 0,138"/>
    <polygon class="stripe" points="125,0 159,0 19,214 0,214 0,191"/>
    <polygon class="stripe" points="324,0 296,0 379,127 379,84"/>
    <polygon class="stripe" points="289,0 262,0 379,179 379,138"/>
    <polygon class="stripe" points="254,0 220,0 360,214 379,214 379,191"/>
  </svg>
  <div class="card__content">
    <div class="wordmark">Ostrel Appraisals</div>
    <div class="holder">
      <div class="holder__name">Maarten Vos, CFA, ASA, RV</div>
      <div class="holder__role">Managing Director</div>
    </div>
  </div>
</section>

<section class="card card--back" aria-label="Business card back">
  <svg class="card__stripes" viewBox="0 0 379 214" preserveAspectRatio="none" aria-hidden="true">
    <polygon class="stripe" points="55,0 83,0 0,127 0,84"/>
    <polygon class="stripe" points="90,0 117,0 0,179 0,138"/>
    <polygon class="stripe" points="125,0 159,0 19,214 0,214 0,191"/>
    <polygon class="stripe" points="324,0 296,0 379,127 379,84"/>
    <polygon class="stripe" points="289,0 262,0 379,179 379,138"/>
    <polygon class="stripe" points="254,0 220,0 360,214 379,214 379,191"/>
  </svg>
  <div class="card__content">
    <div class="wordmark">Ostrel Appraisals</div>
    <div class="tagline">Business and intellectual<br>property valuations</div>
    <div class="contacts">
      <div class="contacts__row">
        <span class="contact">
          <svg viewBox="0 0 24 24" aria-hidden="true"><path d="M12 2a10 10 0 1 0 0 20 10 10 0 0 0 0-20zm7.9 9h-3.4a15 15 0 0 0-1.3-5.6A8 8 0 0 1 19.9 11zM12 4c.9 1.2 2.1 3.6 2.4 7H9.6C9.9 7.6 11.1 5.2 12 4zM8.8 5.4A15 15 0 0 0 7.5 11H4.1a8 8 0 0 1 4.7-5.6zM4.1 13h3.4a15 15 0 0 0 1.3 5.6A8 8 0 0 1 4.1 13zM12 20c-.9-1.2-2.1-3.6-2.4-7h4.8c-.3 3.4-1.5 5.8-2.4 7zm3.2-1.4a15 15 0 0 0 1.3-5.6h3.4a8 8 0 0 1-4.7 5.6z"/></svg>
          www.ostrelappraisals.com
        </span>
        <span class="contact">
          <svg viewBox="0 0 24 24" aria-hidden="true"><path d="M6.6 10.8a15 15 0 0 0 6.6 6.6l2.2-2.2a1 1 0 0 1 1-.25 11.4 11.4 0 0 0 3.6.57 1 1 0 0 1 1 1V20a1 1 0 0 1-1 1A17 17 0 0 1 3 4a1 1 0 0 1 1-1h3.5a1 1 0 0 1 1 1c0 1.25.2 2.45.57 3.57a1 1 0 0 1-.25 1z"/></svg>
          +31 (0)71 555 0142
        </span>
        <span class="contact">
          <svg viewBox="0 0 24 24" aria-hidden="true"><path d="M2 5h20v14H2zm2 2v.5l8 5 8-5V7l-8 5z"/></svg>
          mvos@ostrelappraisals.com
        </span>
      </div>
      <div class="contacts__row">
        <span class="contact">
          <svg viewBox="0 0 24 24" aria-hidden="true"><path d="M12 2a7 7 0 0 0-7 7c0 5.2 7 13 7 13s7-7.8 7-13a7 7 0 0 0-7-7zm0 9.5A2.5 2.5 0 1 1 12 6.5a2.5 2.5 0 0 1 0 5z"/></svg>
          Molenvlietkade 27, 4817 KT Leiden, The Netherlands
        </span>
      </div>
    </div>
  </div>
</section>

</body>
</html>
```